Ferlande Glues

Website for funeral directors see the original website: http://pates-ferlande.be
Target Market(s)
B2C
Coding
Coded - Design and coding required
Number of Pages Required
5+ page
Font styles to use
Serif
Sans Serif
Script
Colors
9d9d9d
757575
e667a6
eea4c8
e34197
Requirements
Must have
- Keep the architecture of the current site.
Nice to have
- A page with a list of people who have died. See example: https://www.maisonbrevant.be

```html
<!DOCTYPE html>
<html lang="en">
<head>
<meta charset="utf-8">
<title>Ferlande Glues – Funeral Directors</title>
<link href="https://fonts.googleapis.com/css2?family=Poppins:wght@400;500;600&family=Lobster+Two:ital,wght@1,700&family=Tinos&family=Great+Vibes&display=swap" rel="stylesheet">
<style>
:root{
  --pink:#e34197;
  --pink-mid:#e667a6;
  --pink-soft:#eea4c8;
  --grey-light:#9d9d9d;
  --grey:#757575;
  --ink:#1d1d1d;
  --text:#4a4a4a;
  --white:#fff;
  --nav:#5e5e5e;
}
*{margin:0;padding:0;box-sizing:border-box}
html,body{width:755px;height:1200px;overflow:hidden}
body{position:relative;background:var(--white);font-family:'Poppins',sans-serif;color:var(--text)}
.abs{position:absolute}

/* header */
.topbar{left:0;top:0;width:755px;height:51px;background:linear-gradient(90deg,#e0479b,#e55aa6 50%,#e0479b)}
.brand{left:148px;top:12px;display:flex;align-items:center;gap:7px;color:var(--white)}
.brand-dot{width:26px;height:26px;border-radius:50%;border:2px solid var(--white)}
.brand-name{font-family:'Poppins',sans-serif;font-weight:600;font-size:11px;letter-spacing:.2px}
.top-info{top:17px;display:flex;align-items:center;gap:6px;color:var(--white);font-size:8px;line-height:10px}
.top-info b{font-weight:600}
.addr{left:390px}
.phone{left:505px}

.nav{left:0;top:51px;width:755px;height:19px;background:linear-gradient(#6a6a6a,#4f4f4f);display:flex;justify-content:center;align-items:center}
.nav a{color:var(--white);text-decoration:none;font-size:6.4px;text-transform:uppercase;padding:0 9px;border-left:1px solid #7c7c7c;line-height:8px}
.nav a:first-child{border-left:none}
.nav small{font-size:5px}

/* hero */
.hero{left:0;top:70px}
.slogan{left:0;top:160px;width:755px;text-align:center;font-family:'Lobster Two',cursive;font-style:italic;font-weight:700;font-size:15.5px;line-height:19px;color:var(--white);text-shadow:0 1px 3px rgba(0,0,0,.5)}
.hero-btn{left:322px;top:212px;width:112px;height:23px;border:1.5px solid var(--white);border-radius:12px;color:var(--white);font-size:7.8px;font-weight:500;letter-spacing:.4px;display:flex;align-items:center;justify-content:center}
.dots{left:361px;top:302px;display:flex;gap:4px}
.dots span{width:8px;height:8px;border-radius:50%;border:1px solid var(--white)}
.dots span:first-child{background:var(--white)}

/* sections */
.section-title{left:0;width:755px;text-align:center;font-weight:600;font-size:14px;color:var(--ink)}
.rule{left:363px;width:28px;height:1px;background:var(--pink)}
.copy{left:185px;width:385px;text-align:center;font-size:6.5px;line-height:10.2px;color:var(--text)}
.btn-pink-outline{left:339px;top:538px;width:77px;height:25px;border:1px solid var(--pink);color:var(--pink);font-size:7px;font-weight:500;display:flex;align-items:center;justify-content:center}

.card{top:678px;width:146px}
.card .photo{width:146px;height:98px}
.card .bar{margin-top:5px;height:26px;background:var(--pink);color:var(--white);font-size:6.3px;font-weight:600;display:flex;align-items:center;justify-content:center;text-transform:uppercase}
.card p{margin-top:9px;font-size:6.4px;line-height:10px;color:var(--grey);height:20px;overflow:hidden}
.card .more{margin-top:11px;width:75px;height:22px;border:1px solid #cfcfcf;font-size:6.4px;font-weight:500;letter-spacing:.8px;color:var(--grey);display:flex;align-items:center;justify-content:center}

/* call to action */
.cta{left:0;top:894px;width:755px;height:144px}
.cta-text{left:0;top:930px;width:755px;text-align:center;font-family:'Tinos',serif;font-size:12.5px;line-height:14.5px;color:var(--white)}
.cta-phone{left:256px;top:977px;width:128px;height:23px;background:var(--pink);color:var(--white);font-family:'Tinos',serif;font-size:11.5px;display:flex;align-items:center;justify-content:center}
.cta-contact{left:389px;top:977px;width:111px;height:23px;border:1px solid var(--white);color:var(--white);font-family:'Tinos',serif;font-size:9px;display:flex;align-items:center;justify-content:center}

/* footer */
.foot-brand{left:148px;top:1072px;display:flex;align-items:center;gap:7px;color:var(--ink)}
.foot-brand .brand-dot{border-color:var(--ink)}
.social{left:184px;top:1111px;display:flex;gap:4px}
.social span{width:11px;height:11px;border-radius:50%;background:var(--grey-light)}
.foot-col{top:1066px;font-size:5.6px;line-height:10px;color:var(--text)}
.foot-col h4{font-size:6.3px;font-weight:500;color:var(--ink);margin-bottom:10px;letter-spacing:.2px}
.ci{display:flex;gap:5px;margin-bottom:5px;align-items:flex-start}
.ci svg{flex:none;margin-top:2px}
.newsletter-form{margin-top:10px;width:111px;height:19px;border:1px solid #bcbcbc;display:flex;align-items:center;justify-content:space-between;padding-left:5px;font-size:5.6px;color:var(--text)}
.newsletter-form span.btn{height:15px;width:35px;margin-right:1px;background:var(--grey);color:var(--white);font-weight:600;font-size:5.4px;display:flex;align-items:center;justify-content:center}
.foot-rule{left:148px;top:1163px;width:460px;height:1px;background:#d8d8d8}
.copyright{left:0;top:1178px;width:755px;text-align:center;font-size:5.4px;color:var(--grey-light)}
</style>
</head>
<body>

<header>
  <div class="abs topbar"></div>
  <div class="abs brand"><span class="brand-dot"></span><span class="brand-name">Ferlande Glues</span></div>
  <div class="abs top-info addr">
    <svg width="13" height="18" viewBox="0 0 13 18"><path d="M6.5 0C2.9 0 0 2.8 0 6.3 0 11 6.5 18 6.5 18S13 11 13 6.3C13 2.8 10.1 0 6.5 0z" fill="#fff"/><circle cx="6.5" cy="6.3" r="2.6" fill="#e34197"/></svg>
    <div><b>rue des Tilleuls 48</b><br><b>4520 VALMONT</b></div>
  </div>
  <div class="abs top-info phone">
    <svg width="11" height="18" viewBox="0 0 11 18"><rect x="1" y="1" width="9" height="16" rx="1.5" fill="none" stroke="#fff" stroke-width="1.6"/><line x1="1" y1="13" x2="10" y2="13" stroke="#fff" stroke-width="1.2"/></svg>
    <div>CALL US TODAY<br><b>+32 (0) 61 / 48.30.17</b></div>
  </div>
  <nav class="abs nav">
    <a>Home</a><a>Our Society <small>⌄</small></a><a>What to do in case of death? <small>⌄</small></a><a>Our Services <small>⌄</small></a><a>They have left us</a><a>Contact</a>
  </nav>
</header>

<section>
  <svg class="abs" style="left:0;top:0" width="755" height="1200" viewBox="0 0 755 1200">
    <defs>
      <linearGradient id="fog" x1="0" y1="0" x2="0" y2="1">
        <stop offset="0" stop-color="#eceef2"/><stop offset=".5" stop-color="#ffffff"/><stop offset="1" stop-color="#e9eaee"/>
      </linearGradient>
      <linearGradient id="heroFill" x1="0" y1="0" x2="1" y2="0">
        <stop offset="0" stop-color="#8d8d8f"/><stop offset=".35" stop-color="#4d4d52"/><stop offset=".7" stop-color="#2c2c30"/><stop offset="1" stop-color="#6e6c6a"/>
      </linearGradient>
    </defs>
    <rect x="0" y="300" width="755" height="280" fill="url(#fog)" role="img" aria-label="Misty winter landscape with bare trees"/>
    <path role="img" aria-label="Black hearse parked in front of a stone church" d="M0 70H755V405C650 350 520 312 430 324C330 338 260 368 180 362C95 356 35 320 0 288Z" fill="url(#heroFill)"/>
    <path d="M755 405C650 350 520 312 430 324C330 338 260 368 180 362C95 356 35 320 0 288" fill="none" stroke="#e34197" stroke-width="2.5"/>
  </svg>
  <div class="abs slogan">The tree owes the beauty of its fruits to the strength<br>of its bark and the wisdom of its roots ...</div>
  <div class="abs hero-btn">CONTACT US TODAY</div>
  <div class="abs dots"><span></span><span></span><span></span></div>
</section>

<section>
  <h2 class="abs section-title" style="top:395px">About Ferlande Glues Funerailles</h2>
  <div class="abs rule" style="top:421px"></div>
  <p class="abs copy" style="top:438px">Lorem ipsum dolor sit amet, consectetur adipiscing elit. Aliquam justo ligula, mattis quis sollicitudin et, pretium ac sapien. Sed sit amet consectetur ex. Sed sit amet sem porta, fringilla sapien ac, dapibus justo. Praesent efficitur ac odio eu ultricies. Pellentesque ultrices nisl in vulputate gravida. Nullam ultricies faucibus aliquam.</p>
  <p class="abs copy" style="top:479px">Nunc id commodo felis. Maecenas rutrum enim tincidunt tempor sagittis. Praesent eget pretium turpis, eget cursus mauris. Vestibulum vel ligula quis risus molestie scelerisque. Quisque elementum congue nunc, quis vulputate purus gravida sit amet. Nunc nec blandit enim, et interdum nisi. Ut vitae orci justo. Phasellus rhoncus lacus enim, pulvinar mollis neque venenatis id. Nunc eget magna et dui facilisis tempor pharetra sed tellus.</p>
  <div class="abs btn-pink-outline">READ MORE</div>
</section>

<section>
  <h2 class="abs section-title" style="top:588px">Our Services</h2>
  <div class="abs rule" style="top:615px"></div>
  <p class="abs copy" style="top:632px">Phasellus rhoncus mollis purus, vel vestibulum diam congue id. Orci varius natoque penatibus et magnis dis parturient montes, nascetur ridiculus mus. Curabitur imperdiet, enim in cursus pharetra, dui odio maximus arcu, a ullamcorper velit ligula et magna. Proin eget lacinia ligula, ut malesuada augue.</p>

  <article class="abs card" style="left:148px">
    <div class="photo" role="img" aria-label="Black hearse in front of a church" style="background:linear-gradient(#b9b2a4,#6f6b66 55%,#1c1c1e 75%,#8a8680)"></div>
    <div class="bar">Complete funeral organization</div>
    <p>Our first concern is to simplify the decision making made very difficult in a moment</p>
    <div class="more">READ MORE</div>
  </article>
  <article class="abs card" style="left:305px">
    <div class="photo" role="img" aria-label="Smiling senior couple outdoors" style="background:linear-gradient(90deg,#7fa64a,#d9c3a8 45%,#e8d8c5 70%,#8fb153)"></div>
    <div class="bar">Plan your funeral in advance</div>
    <p>By organizing your funeral in advance, you freely decide in detail how your funeral will be</p>
    <div class="more">READ MORE</div>
  </article>
  <article class="abs card" style="left:463px">
    <div class="photo" role="img" aria-label="White flower arrangement with a ribbon" style="background:linear-gradient(135deg,#6f9a48,#e9ead8 45%,#f4f1e6 60%,#7ea24e)"></div>
    <div class="bar">Have your flowers delivered online</div>
    <p>Order your natural flowers and silk flowers directly through our website, we deliver to the</p>
    <div class="more">READ MORE</div>
  </article>
</section>

<section>
  <div class="abs cta" role="img" aria-label="Lit candle beside white roses" style="background:linear-gradient(90deg,#1a1612,#3a3129 25%,#1c1b1a 45%,#2d3a2a 70%,#6c7d61)"></div>
  <p class="abs cta-text">Pellentesque non eros in magna bibendum tempor at sed metus.<br>Donec tincidunt, turpis quis aliquet sodales</p>
  <div class="abs cta-phone">+32 (0) 61 / 48.30.17</div>
  <div class="abs cta-contact">CONTACT US TODAY</div>
</section>

<footer>
  <div class="abs foot-brand"><span class="brand-dot"></span><span class="brand-name">Ferlande Glues</span></div>
  <div class="abs social" aria-label="Social networks"><span></span><span></span><span></span><span></span></div>

  <div class="abs foot-col" style="left:296px">
    <h4>CONTACT INFO</h4>
    <div class="ci"><svg width="6" height="8" viewBox="0 0 6 8"><path d="M3 .5C1.6.5.5 1.6.5 2.9.5 4.8 3 7.5 3 7.5S5.5 4.8 5.5 2.9C5.5 1.6 4.4.5 3 .5z" fill="none" stroke="#757575" stroke-width=".7"/></svg><span>rue des Tilleuls 48<br>4520 VALMONT</span></div>
    <div class="ci"><svg width="7" height="7" viewBox="0 0 7 7"><path d="M1 .8l1.3-.2.7 1.6-.8.6c.4.9 1 1.5 1.9 1.9l.6-.8 1.6.7-.2 1.3C3.3 6 .9 3.6 1 .8z" fill="none" stroke="#757575" stroke-width=".6"/></svg><span>+ 32.61 / 48.30.17</span></div>
    <div class="ci"><svg width="7" height="6" viewBox="0 0 7 6"><rect x=".4" y=".6" width="6.2" height="4.6" fill="none" stroke="#757575" stroke-width=".6"/><path d="M.4.6 3.5 3.3 6.6.6" fill="none" stroke="#757575" stroke-width=".6"/></svg><span>contact@pfglues.be</span></div>
  </div>

  <div class="abs foot-col" style="left:391px">
    <h4>Quick Links</h4>
    Home<br>Our Society<br>What to do in Case of Death?<br>Our Services<br>They Have left Us<br>Contact
  </div>

  <div class="abs foot-col" style="left:499px">
    <h4>Sign Up For Newsletter</h4>
    Lorem ipsum dolor sit amet, consectetur<br>adipiscing elit
    <div class="newsletter-form"><span>Enter email</span><span class="btn">SIGN UP</span></div>
  </div>

  <div class="abs foot-rule"></div>
  <p class="abs copyright">Copyright © 2019 Pompes Funèbres Ferlande Glues. All right Reserved.</p>
</footer>

</body>
</html>
```